Business Card Design

I want something very modern, Im from the gold coast Australia double sided and using my attached logo, a mix of cameras or a close up, I will attach pics, no logo please from other manufacturers, only Guard Every Nook, I want to promote a individual approach to security, My logo is - Honest Advise Without The Price - :)

Target Market(s)

Anyone that handles money or wants to secure there premises

Industry/Entity Type

Business

Contact Information for Business Card

Marcus Dale finch
Guard Every Nook
Brookvale Heights Queensland 4299
Mobile : 0431 587 902 & VoIP +610431587902
Security Provider Licence QLD - 5829143
Free Quotes
CCTV, Alarms, Digital Cameras, RFID, - In Home Design

Colors

Designer to choose colors to be used in the design.

Requirements
Must have
• Free Quotes
On Site Design
Full details And Licence number Etc
Should not have
• I know these are low res pics, im waiting to receive stock before taking new photos

```html
<!DOCTYPE html>
<html lang="en">
<head>
<meta charset="utf-8">
<title>Guard Every Nook – Business Card</title>
<link href="https://fonts.googleapis.com/css2?family=Michroma&family=Exo+2:wght@300&display=swap" rel="stylesheet">
<style>
  :root {
    --backdrop: #1d1e21;
    --card: #2b2f36;
    --ink-light: #f2f3f5;
    --ink-soft: #b9bec7;
    --frame-line: #8e949e;
    --panel: #9a9ea6;
    --panel-deep: #7f848d;
    --brand-mark: #c9463d;
  }
  * { margin: 0; padding: 0; box-sizing: border-box; }
  html, body { width: 1200px; height: 1200px; overflow: hidden; background: var(--backdrop); }
  .sheet {
    width: 1200px; height: 1200px;
    display: flex; flex-direction: column; align-items: center; justify-content: center; gap: 60px;
  }
  .card {
    position: relative; width: 900px; height: 514px;
    background: var(--card); overflow: hidden;
    box-shadow: 0 18px 40px rgba(0,0,0,.45);
  }
  .frame-corners { position: absolute; inset: 0; }
  .holder-name {
    position: absolute; left: 150px; top: 196px;
    font-family: "Michroma", sans-serif; font-size: 34px; letter-spacing: 6px;
    color: var(--ink-light);
  }
  .contact {
    position: absolute; left: 150px; top: 300px;
    font-family: "Exo 2", sans-serif; font-weight: 300; font-size: 21px; letter-spacing: 2px;
    color: var(--ink-soft); line-height: 30px;
  }
  .contact .indent { padding-left: 170px; display: block; }
  .product-panel { position: absolute; inset: 0; }
  .brand {
    position: absolute; left: 90px; top: 250px;
    display: flex; align-items: center; gap: 14px;
    font-family: "Exo 2", sans-serif; font-weight: 300; font-size: 22px; letter-spacing: 3px;
    color: var(--ink-light); text-transform: uppercase;
  }
  .brand .mark { width: 18px; height: 18px; background: var(--brand-mark); }
  .services {
    position: absolute; left: 120px; top: 412px;
    font-family: "Exo 2", sans-serif; font-weight: 300; font-size: 20px; letter-spacing: 2px;
    color: var(--ink-soft); line-height: 30px;
  }
</style>
</head>
<body>
<main class="sheet">
  <section class="card card-front">
    <svg class="frame-corners" width="900" height="514" viewBox="0 0 900 514" aria-hidden="true">
      <g fill="none" stroke="var(--frame-line)" stroke-width="1.2">
        <polyline points="40,80 40,40 90,40"/>
        <polyline points="800,40 860,40 860,80"/>
        <polyline points="860,434 860,474 800,474"/>
        <polyline points="40,434 40,474 100,474"/>
      </g>
    </svg>
    <h1 class="holder-name">MARCUS DALE</h1>
    <p class="contact">
      finch Guard Every Nook Brookvale Heights Queensland 4299
      <span class="indent">Mobile: 0431 587 902</span>
      <span class="indent">VoIP: +610431587902</span>
    </p>
  </section>

  <section class="card card-back">
    <svg class="product-panel" width="900" height="514" viewBox="0 0 900 514">
      <defs>
        <linearGradient id="panelShade" x1="0" y1="0" x2="1" y2="1">
          <stop offset="0" stop-color="var(--panel)"/>
          <stop offset="1" stop-color="var(--panel-deep)"/>
        </linearGradient>
      </defs>
      <polygon points="440,30 900,30 900,232 492,344" fill="url(#panelShade)"
               role="img" aria-label="Photo of security cameras: bullet, dome and wall-mounted CCTV units"/>
    </svg>
    <div class="brand"><span class="mark"></span>Guard Every Nook</div>
    <p class="services">
      Security Provider Licence QLD - 5829143 Free Quotes CCTV<br>
      Alarms, Digital Cameras, RFID, - In Home Design
    </p>
  </section>
</main>
</body>
</html>
```